Pediatric Dentist Website

We need a photoshop mockup of one page of a pediatric dentist website. This site will not have an intro page. This layout will need to work for all 4 pages of the final site.

We just finished creating a logo for this practice. It should be attached.

The name of the practice is:

Pediatric Dentistry of Calloway

The doctor''s name is:

Martin Kowalczyk, DMD

There needs to have a menu with 4 pages on it.

Home

Meet the Doctor

Our Office

Contact Us

Please use sample text on the page.

A pediatric dentist is a dentist who specializes in treating kids, so feel free to use pictures of kids in the design.

Design Information:

The doctor likes the following sites:

http://www.plumtreekidsdds.example/

http://www.drmarisoldds.example/

http://drortonwhitfield.example/

http://toothgrovecorner.example/

Their office has an outdoors, woodsy, camping, rustic feel to it. He would like the website to portray that if possibly.

Please do not include stick figure people in it like the following websites:

http://www.arnoldvantedds.example/

http://littlemolarhub.example/

He does not like these sites. He called them too cartoonish.

For the address and phone, please use

742 Quarry Lane

Anytown, GA, 30987

Phone: (877) 555-0142

Fax: (877) 555-0142

If we pick your design, we will most likely need you to modify some small details on it.

We will also need the development files for this.

Fax: (877) 555-0142
Updates

Please be sure to use the logo we have provided. Also, colors should compliment the logo.

The sample design should be of the home page. You can use kids or a mom and kid(s) or a photo of "the office" as an example with the home page text.

So far the designs I''ve seen are okay. They all need a lot of work before I can present them to my client. Things to keep in mind: They will be adding pages later on to expand their website, so the menu needs to be down the left-hand side. 

Although the doctor didn''t specify this site as one of the sites he liked, I like it for an example of the format of the site: http://www.clearpebblegrins.example/. Also, this is one that the doctor did say that he liked: http://drortonwhitfield.example/

The text needs to be on a white or cream background. Having it be on other colors gets too hard to read and looks unprofessional.

Keep in mind this is going to be a full website. Most of the designs I''ve seen so far have been too small to expand into a full website.

Target Market(s)

Parents of kids and kids themselves.

```html
<!DOCTYPE html>
<html lang="en">
<head>
<meta charset="utf-8">
<title>Pediatric Dentistry of Calloway</title>
<link rel="stylesheet" href="https://fonts.googleapis.com/css2?family=Cabin+Sketch:wght@700&family=Patrick+Hand+SC&display=swap">
<style>
  :root {
    --cyan: #3fd0f0;
    --cyan-pale: #b3eff8;
    --blue: #1a6fc0;
    --blue-deep: #1d3f9c;
    --lime: #8fd620;
    --note: #a9e6f6;
    --note-tape: #c9f1fa;
    --paper: #ebeae2;
    --paper-edge: #d9d8ce;
    --ink: #1a1a1a;
    --bark: #6b3a1a;
    --grass: #7fd12a;
    --white: #ffffff;
  }
  * { box-sizing: border-box; margin: 0; padding: 0; }
  html, body { width: 1200px; height: 900px; overflow: hidden; background: var(--white); }
  .page { position: relative; width: 1200px; height: 900px; overflow: hidden; font-family: "Patrick Hand SC", "Comic Sans MS", cursive; }

  .color-bar { position: absolute; top: 0; left: 0; width: 1200px; height: 21px; display: flex; }
  .color-bar span { height: 100%; }
  .color-bar .c1 { width: 308px; background: var(--cyan); }
  .color-bar .c2 { width: 330px; background: var(--cyan-pale); }
  .color-bar .c3 { width: 300px; background: var(--blue); }
  .color-bar .c4 { width: 262px; background: var(--lime); }

  .brand { position: absolute; left: 48px; top: 120px; width: 220px; display: flex; align-items: center; gap: 10px; color: var(--blue); font-size: 27px; line-height: 1.05; }
  .brand-dot { flex: none; width: 34px; height: 34px; border-radius: 50%; background: var(--cyan); }

  .sky { position: absolute; border-radius: 40px; background: linear-gradient(#e6f8fc, #d3f1f9); }
  .sky-1 { left: 488px; top: 48px; width: 100px; height: 30px; }
  .sky-2 { left: 765px; top: 54px; width: 80px; height: 28px; }
  .sky-3 { left: 878px; top: 98px; width: 170px; height: 48px; background: linear-gradient(#d4e6f8, #c2dbf4); }
  .sky-4 { left: 1083px; top: 56px; width: 80px; height: 26px; }
  .sky-5 { left: 818px; top: 172px; width: 95px; height: 30px; }
  .sky-6 { left: 555px; top: 170px; width: 50px; height: 22px; }

  .snapshot { position: absolute; padding: 14px 14px 30px; box-shadow: 2px 3px 6px rgba(0,0,0,.15); }
  .snapshot .photo { width: 100%; height: 100%; }
  .snapshot-blue { left: 345px; top: 100px; width: 172px; height: 176px; background: var(--blue); transform: rotate(-2deg); }
  .snapshot-blue .photo { background: linear-gradient(160deg, #9dd3f2, #d8b59a 60%, #7a5a44); }
  .snapshot-green { left: 568px; top: 86px; width: 178px; height: 190px; background: var(--lime); transform: rotate(4deg); }
  .snapshot-green .photo { background: linear-gradient(160deg, #f2f2ee, #d9c8ad 60%, #b89b7a); }
  .tape { position: absolute; height: 22px; background: rgba(63,208,240,.45); }

  .bird-branch { position: absolute; left: 925px; top: 150px; width: 215px; height: 165px; background: linear-gradient(160deg, #bff0f8 0%, #8fe0f0 50%, #c9a58a 100%); border-radius: 50% 40% 30% 60%; opacity: .8; }

  .nav-note { position: absolute; left: 60px; top: 378px; width: 338px; height: 312px; background: var(--note); transform: rotate(-1deg); box-shadow: 0 0 0 10px rgba(169,230,246,.35); }
  .nav-note .tape { top: -16px; left: 30px; width: 150px; transform: rotate(-8deg); background: rgba(201,241,250,.85); }
  .main-nav { position: absolute; left: 98px; top: 420px; list-style: none; }
  .main-nav li { height: 60px; }
  .main-nav a { color: var(--blue); text-decoration: none; font-family: "Cabin Sketch", "Comic Sans MS", cursive; font-size: 28px; letter-spacing: 1px; white-space: nowrap; }
  .main-nav li:nth-child(3) { padding-left: 7px; }
  .main-nav li:nth-child(4) { padding-left: 19px; }
  .chat-icon { position: absolute; left: 292px; top: 578px; }

  .content { position: absolute; left: 432px; top: 318px; width: 735px; height: 492px; background: linear-gradient(90deg, var(--paper), #f1f0ea 70%, var(--paper-edge)); box-shadow: 2px 3px 8px rgba(0,0,0,.12); }
  .content .holes { position: absolute; right: 14px; top: 20px; bottom: 20px; width: 14px; background: radial-gradient(circle, var(--white) 5px, transparent 6px) 0 0 / 14px 34px repeat-y; }
  .content h1 { position: absolute; top: 26px; left: 0; width: 700px; text-align: center; font-family: "Cabin Sketch", "Comic Sans MS", cursive; font-size: 36px; letter-spacing: 2px; color: var(--ink); }
  .content .copy { position: absolute; top: 76px; left: 26px; width: 652px; color: var(--ink); font-size: 16px; line-height: 32px; text-align: center; }
  .content .copy p + p { margin-top: 28px; }

  .meadow { position: absolute; left: 0; top: 790px; width: 1200px; height: 110px; background: linear-gradient(rgba(127,209,42,0), var(--grass) 45%, #5fb81e); }
  .sprigs { position: absolute; left: 30px; top: 720px; width: 240px; height: 110px; background: linear-gradient(rgba(143,214,32,0), rgba(143,214,32,.55)); border-radius: 40% 40% 0 0; }

  .site-footer { position: absolute; left: 465px; top: 832px; width: 642px; height: 57px; background: var(--white); border: 3px solid var(--bark); border-radius: 10px; color: var(--blue-deep); font-size: 14px; line-height: 22px; text-align: center; padding-top: 4px; letter-spacing: .3px; }
</style>
</head>
<body>
<div class="page">
  <div class="color-bar"><span class="c1"></span><span class="c2"></span><span class="c3"></span><span class="c4"></span></div>

  <div class="brand"><span class="brand-dot"></span><span>Pediatric Dentistry of Calloway</span></div>

  <div class="sky sky-1" role="img" aria-label="Drawn cloud"></div>
  <div class="sky sky-2" role="img" aria-label="Drawn cloud"></div>
  <div class="sky sky-3" role="img" aria-label="Drawn cloud"></div>
  <div class="sky sky-4" role="img" aria-label="Drawn cloud"></div>
  <div class="sky sky-5" role="img" aria-label="Drawn cloud"></div>
  <div class="sky sky-6" role="img" aria-label="Drawn cloud"></div>

  <figure class="snapshot snapshot-blue">
    <div class="photo" role="img" aria-label="Photo of two smiling young brothers"></div>
  </figure>
  <figure class="snapshot snapshot-green">
    <div class="photo" role="img" aria-label="Photo of a cheerful girl reaching out"></div>
  </figure>
  <span class="tape" style="left:330px;top:92px;width:90px;transform:rotate(-6deg)"></span>
  <span class="tape" style="left:650px;top:70px;width:90px;transform:rotate(-10deg);background:rgba(143,214,32,.5)"></span>

  <div class="bird-branch" role="img" aria-label="Illustration of a blue bird perched on a curling branch"></div>

  <div class="nav-note"><span class="tape"></span></div>
  <ul class="main-nav">
    <li><a href="#">HOME</a></li>
    <li><a href="#">MEET THE DOCTOR</a></li>
    <li><a href="#">OUR OFFICE</a></li>
    <li><a href="#">CONTACT US</a></li>
  </ul>
  <svg class="chat-icon" width="66" height="44" viewBox="0 0 66 44" aria-hidden="true">
    <path d="M14 4h40a10 10 0 0 1 10 10v6a10 10 0 0 1-10 10H26l-14 10 4-10h-2A10 10 0 0 1 4 20v-6A10 10 0 0 1 14 4z" fill="#d6f4fb" stroke="#7fd5ee" stroke-width="2"/>
  </svg>

  <main class="content">
    <span class="holes"></span>
    <h1>WELCOME</h1>
    <div class="copy">
      <p>LOREM IPSUM DOLOR SIT AMET, CONSECTETUR ADIPISICING ELIT, SED DO EIUSMOD TEMPOR INCIDIDUNT UT LABORE ET DOLORE MAGNA ALIQUA. UT ENIM AD MINIM VENIAM, QUIS NOSTRUD EXERCITATION ULLAMCO LABORIS NISI UT ALIQUIP EX EA COMMODO CONSEQUAT. DUIS AUTE IRURE DOLOR IN REPREHENDERIT IN VOLUPTATE VELIT ESSE CILLUM DOLORE EU FUGIAT NULLA PARIATUR. EXCEPTEUR SINT OCCAECAT CUPIDATAT NON PROIDENT, SUNT IN CULPA QUI OFFICIA DESERUNT MOLLIT ANIM ID EST LABORUM.</p>
      <p>SED UT PERSPICIATIS UNDE OMNIS ISTE NATUS ERROR SIT VOLUPTATEM ACCUSANTIUM DOLOREMQUE LAUDANTIUM, TOTAM REM APERIAM, EAQUE IPSA QUAE AB ILLO INVENTORE VERITATIS ET QUASI ARCHITECTO BEATAE VITAE DICTA SUNT EXPLICABO. NEMO ENIM IPSAM VOLUPTATEM QUIA VOLUPTAS SIT ASPERNATUR AUT ODIT AUT FUGIT, SED QUIA CONSEQUUNTUR MAGNI DOLORES EOS QUI RATIONE VOLUPTATEM SEQUI NESCIUNT. NEQUE PORRO QUISQUAM EST, QUI DOLOREM IPSUM QUIA DOLOR SIT AMET, CONSECTETUR, ADIPISCI VELIT, SED QUIA NON NUMQUAM EIUS MODI TEMPORA INCIDU</p>
    </div>
  </main>

  <div class="meadow" role="img" aria-label="Illustrated green grass along the bottom"></div>
  <div class="sprigs" role="img" aria-label="Illustrated wild flowers and sprigs"></div>

  <footer class="site-footer">
    742 QUARRY LANE ,ANYTOWN, GA, 30987 &nbsp; PHONE: (877) 555-0142 &nbsp;FAX: (877) 555-0142<br>
    COPYRIGHT © 2009 MARTIN KOWALCZYK, DMD. - PEDIATRIC DENTIST &nbsp;ALL RIGHTS RESERVED.
  </footer>
</div>
</body>
</html>
```